Create a flyer for our party getaway to Ibiza.

'The Crimson Ibiza Escape'

Friday 14th July - Monday 17th July

DJ Morvek & DJ Tundral brings together a jam-packed weekend schedule full of the best urban parties in Ibiza.

What's included?

4 Nights Of Entertainment
6 Parties In Total
1 Boat Party
1 Pool Party
2 Superclub Parties
1 Indoor Water Party
Bottomless Drinks (Boat Party Only)
An unbelievable experience
1 unbeatable price.

All this for 140€ (you save 50€ when you book with us)

Tickets avaialble from Ticketlane & Gribolo

Target Market(s)

holiday goers

Industry/Entity Type

party, events, club, hip hop

Requirements
Must have
• good vibes
Nice to have
• nice catchy looking title

```html
<!DOCTYPE html>
<html lang="en">
<head>
<meta charset="utf-8">
<title>The Crimson Ibiza Escape</title>
<link href="https://fonts.googleapis.com/css2?family=Anton&family=Arimo:wght@400;700&family=Montserrat:wght@300;400;700&display=swap" rel="stylesheet">
<style>
  :root {
    --backdrop: #dcdcdc;
    --crimson: #e8291f;
    --crimson-deep: #a8191f;
    --night: #1f1c22;
    --flame: #f57a1e;
    --white: #ffffff;
    --photo-a: #1a2140;
    --photo-b: #4a2a4f;
    --photo-c: #8b2a2e;
  }
  * { margin: 0; padding: 0; box-sizing: border-box; }
  html, body { width: 1200px; height: 800px; overflow: hidden; }
  body { background: var(--backdrop); position: relative; font-family: "Arimo", Arial, sans-serif; }

  .flyer {
    position: absolute; left: 330px; top: 18px;
    width: 540px; height: 764px;
    background: var(--crimson);
    overflow: hidden;
    box-shadow: 0 10px 30px rgba(0,0,0,.25);
  }
  .hero-photo {
    position: absolute; left: 0; top: 0; width: 540px; height: 300px;
    background: linear-gradient(120deg, var(--photo-a) 0%, var(--photo-b) 45%, var(--photo-c) 70%, #2a2d3a 100%);
    border-bottom: 5px solid var(--white);
  }
  .date-column {
    position: absolute; left: 300px; top: 168px; width: 60px; height: 498px;
    background: var(--night);
  }
  .date-column span {
    position: absolute; left: 50%; top: 50%;
    transform: translate(-50%, -50%) rotate(-90deg);
    white-space: nowrap;
    font-family: "Montserrat", sans-serif; font-weight: 300;
    font-size: 21px; letter-spacing: 1px; color: var(--flame);
  }
  .title {
    position: absolute; left: 24px; top: 122px;
    font-family: "Anton", sans-serif; font-size: 40px; line-height: 1; font-weight: 400;
    letter-spacing: .5px; display: flex; gap: 6px;
  }
  .title .word { padding: 4px 8px 5px; color: var(--white); background: var(--crimson); }
  .title .word--dark { background: var(--night); color: var(--crimson); }
  .intro {
    position: absolute; left: 20px; top: 196px; width: 270px;
    text-align: right; color: var(--white);
    font-family: "Arimo", sans-serif; font-weight: 700; font-size: 15px; line-height: 1.25;
    text-shadow: 0 1px 3px rgba(0,0,0,.6);
  }
  .intro .djs { color: var(--flame); font-size: 16px; display: block; }
  .inset-photo {
    position: absolute; left: 378px; top: 322px; width: 146px; height: 180px;
    border: 6px solid var(--white); border-radius: 18px;
    background: linear-gradient(150deg, #3a2d66 0%, #1c1f33 55%, #6b2236 100%);
  }
  .included {
    position: absolute; left: 30px; top: 322px; width: 265px; color: var(--white);
  }
  .included h2 { font-size: 14px; font-weight: 700; margin-bottom: 8px; }
  .included ul { list-style: none; font-size: 13px; line-height: 1.5; }
  .included li { position: relative; padding-left: 16px; }
  .included li::before {
    content: ""; position: absolute; left: 0; top: 6px;
    width: 7px; height: 7px; border: 2px solid var(--white); border-radius: 50%;
  }
  .price {
    position: absolute; left: 30px; top: 560px; width: 265px; text-align: center;
    font-family: "Montserrat", sans-serif; font-size: 12px; line-height: 1.35; color: #ffd9b8;
  }
  .tickets-band {
    position: absolute; left: 0; top: 666px; width: 540px; height: 98px;
    background: var(--crimson-deep);
  }
  .tickets-copy {
    position: absolute; left: 30px; top: 684px;
    font-family: "Montserrat", sans-serif; color: var(--white);
  }
  .tickets-copy small { display: block; font-size: 13px; font-weight: 400; margin-bottom: 6px; }
  .tickets-copy strong { display: block; font-size: 19px; font-weight: 700; }
  .vendors {
    position: absolute; right: 22px; top: 700px;
    display: flex; align-items: center; gap: 22px;
  }
  .vendor {
    display: flex; align-items: center; gap: 8px; white-space: nowrap;
    font-family: "Montserrat", sans-serif; font-weight: 700; font-size: 17px; color: var(--white);
  }
  .vendor .mark { width: 16px; height: 16px; flex: none; }
  .vendor--ticketlane .mark { background: var(--flame); }
  .vendor--gribolo .mark { background: var(--white); }
</style>
</head>
<body>
  <article class="flyer">
    <div class="hero-photo" role="img" aria-label="Photo of the two DJs posing behind the decks in a club"></div>
    <div class="date-column"><span>Friday 14th July - Monday 17th July</span></div>

    <h1 class="title">
      <span class="word">THE CRIMSON</span>
      <span class="word word--dark">IBIZA</span>
      <span class="word">ESCAPE</span>
    </h1>

    <p class="intro">
      <span class="djs">DJ Morvek &amp; DJ Tundral</span>
      brings together a jam-packed weekend schedule full of the best urban parties in Ibiza.
    </p>

    <div class="inset-photo" role="img" aria-label="Photo of a DJ performing at a club party"></div>

    <section class="included">
      <h2>What's included?</h2>
      <ul>
        <li>4 Nights Of Entertainment</li>
        <li>6 Parties In Total</li>
        <li>1 Boat Party</li>
        <li>1 Pool Party</li>
        <li>2 Superclub Parties</li>
        <li>1 Indoor Water Party</li>
        <li>Bottomless Drinks (Boat Party Only)</li>
        <li>An unbelievable experience</li>
        <li>1 unbeatable price.</li>
      </ul>
    </section>

    <p class="price">All this for 140€<br>(you save 50€ when you book with us)</p>

    <div class="tickets-band"></div>
    <div class="tickets-copy">
      <small>Tickets avaialble from :</small>
      <strong>Ticketlane &amp; Gribolo</strong>
    </div>
    <div class="vendors">
      <div class="vendor vendor--ticketlane"><span class="mark"></span>Ticketlane</div>
      <div class="vendor vendor--gribolo"><span class="mark"></span>Gribolo</div>
    </div>
  </article>
</body>
</html>
```